Harbor Lane PEO - Web Build for Professional Employment Organization

We need a website built for our new PEO (professional employment organization). This company will offer third party Human Resource services to companies who are looking to outsource:<br/>Recruiting<br/>Administrative Onboarding<br/>New hire training, ongoing training and development<br/>Payroll/compensation processing/services<br/>Employee Relations<br/>Unemployment Claim Facilitation<br/>Benefits Plans and Administration<br/><br/>I have attached the logo below. Please use that as a reference and color match as best as possible. <br/><br/>Here are some of the competitor's websites:<br/>https://www.workvantrix.com/ <br/>https://www.staffmerola.com/<br/>https://www.staffmerola.com/<br/>https://www.qlr.com/<br/>https://www.hirebendora.com/<br/>https://corvalpeo.com/contact-corval/<br/><br/>

Target Market(s)

Startups and mid-sized businesses

Number of Pages Required

5+ page

Font styles to use
Sans Serif

Colors
0592cd

Requirements
Must have
• Features Pages
• SEO driven keyword rich content
• Strong focus on our ability to provide unemployment claim facilitation services as well as mandatory training/certification fulfillment
Nice to have
• I'd like to see one mockup with a Live Chat version if possible. In theory, the Live Chat messages would go directly to our front desk person.

```html
<!DOCTYPE html>
<html lang="en">
<head>
<meta charset="utf-8">
<title>Harbor Lane PEO</title>
<link href="https://fonts.googleapis.com/css2?family=Roboto:ital,wght@0,300;0,400;0,500;0,700;1,400&display=swap" rel="stylesheet">
<style>
:root{
  --blue:#1a80c4;
  --blue-bright:#0592cd;
  --teal:#1a9bb0;
  --ink:#3a3f4a;
  --text:#5e6470;
  --muted:#8a8f99;
  --navy:#2c3850;
  --navy-deep:#232d42;
  --line:#d8dde3;
  --white:#fff;
  --orange:#e8862a;
}
*{box-sizing:border-box;margin:0;padding:0}
html,body{width:1200px;height:4249px;overflow:hidden}
body{font-family:"Roboto",Arial,sans-serif;color:var(--text);background:var(--white);position:relative}
section,header,footer{position:absolute;left:0;width:1200px}
.abs{position:absolute}
a{color:inherit;text-decoration:none}

/* top bar */
.topbar{top:0;height:40px;background:#f2f4f6}
.topbar ul{position:absolute;right:165px;top:13px;list-style:none;display:flex;gap:26px;font-size:11px;font-weight:500;color:#4a505a}

/* header */
.site-header{top:40px;height:100px;background:var(--white);border-bottom:1px solid #eceff2}
.brand{position:absolute;left:147px;top:30px;display:flex;align-items:center;gap:10px;font-size:26px;font-weight:700;color:var(--blue);letter-spacing:.5px}
.brand-dot{width:18px;height:18px;border-radius:50%;background:var(--blue)}
.main-nav{position:absolute;left:432px;top:46px;display:flex;font-size:14px;font-weight:500;color:#3d434d}
.main-nav a{padding:0 17px;border-left:1px solid #c7ccd2;line-height:14px}
.main-nav a:first-child{padding-left:0;border-left:none;color:var(--blue)}
.nav-marker{position:absolute;left:457px;top:22px;width:14px;height:14px;border-radius:50%;border:2px solid var(--blue)}

/* hero */
.hero{top:140px;height:670px;overflow:hidden}
.hero-photo{position:absolute;inset:0;background:linear-gradient(100deg,#aebfd4 0%,#c7d4e3 30%,#dfe6ee 55%,#cfd6df 100%)}
.hero-title{position:absolute;left:110px;top:214px;width:460px;text-align:center;color:#1f2a3a}
.hero-title .light{font-size:37px;font-weight:300;line-height:43px}
.hero-title .bold{font-size:39px;font-weight:700;line-height:43px}
.btn-solid{position:absolute;left:257px;top:363px;width:167px;height:45px;background:var(--blue);color:#fff;font-size:15px;font-weight:700;display:flex;align-items:center;justify-content:center}
.hero-arrow{position:absolute;top:254px}
.hero-curve{position:absolute;left:0;bottom:0;width:1200px;height:120px}

/* services */
.services{top:810px;height:854px}
.section-title{position:absolute;left:0;width:1200px;text-align:center;font-weight:700}
.services .section-title{top:0;font-size:32px;color:var(--blue)}
.lead{position:absolute;left:250px;width:700px;text-align:center;font-size:14px;line-height:23px;color:#5a606a}
.service{position:absolute;width:296px}
.service.featured{border:1px solid #eef0f3;box-shadow:0 2px 10px rgba(0,0,0,.07);height:278px}
.service svg{position:absolute}
.service h3{position:absolute;font-size:20px;font-weight:700;color:#3a3f4a;line-height:26px}
.service p{position:absolute;font-size:14px;line-height:26px;color:#6b7079}
.btn-outline{position:absolute;border:2px solid var(--blue);color:#2b3340;font-size:15px;font-weight:700;display:flex;align-items:center;justify-content:center;background:#fff}

/* testimonial */
.testimonial{top:1664px;height:576px;overflow:hidden}
.testimonial-photo{position:absolute;inset:0;background:linear-gradient(90deg,#2a3448 0%,#38445a 40%,#8a8f98 62%,#6e6a68 80%,#4a4f5a 100%)}
.testimonial h2{position:absolute;left:139px;top:144px;font-size:28px;font-weight:500;color:#fff}
.testimonial blockquote{position:absolute;left:139px;top:202px;width:425px;font-size:17px;font-style:italic;line-height:29px;color:#eef1f5}
.testimonial .author{position:absolute;left:139px;top:345px;color:#fff;font-size:17px;line-height:24px}
.testimonial .author b{font-weight:700}
.dots{position:absolute;left:140px;top:413px;display:flex;gap:8px}
.dots span{width:45px;height:3px;background:#8b93a3}
.dots span:first-child{background:var(--orange)}

/* courses */
.courses{top:2240px;height:600px;z-index:2}
.courses .section-title{top:92px;font-size:28px;color:var(--ink);font-weight:500}
.course-photo{position:absolute;width:297px;height:218px}
.course-box{position:absolute;width:262px;height:146px;background:#fff;box-shadow:0 2px 10px rgba(0,0,0,.12);text-align:center;padding:30px 18px 0}
.course-box h3{font-size:18px;font-weight:500;color:#2f3541;line-height:20px}
.course-box p{font-size:11px;line-height:19px;color:#8a8f99;margin-top:12px}
.course-box.active{background:var(--blue-bright)}
.course-box.active h3,.course-box.active p{color:#fff}

/* get started */
.get-started{top:2780px;height:582px;background:linear-gradient(90deg,#1a9cae 0%,#1690bd 45%,#1478c4 100%);overflow:hidden;z-index:1}
.gs-curve{position:absolute;left:0;top:0;width:1200px;height:95px}
.emblem{position:absolute;width:52px;height:52px;border-radius:50%;background:#fff;display:flex;align-items:center;justify-content:center}
.emblem span{width:24px;height:24px;border-radius:50%;border:3px solid var(--blue)}
.get-started h2{position:absolute;left:0;width:1200px;top:164px;text-align:center;font-size:28px;font-weight:500;color:#fff}
.get-started .lead{top:212px;color:#e8f4fa;font-size:13px;line-height:20px;left:270px;width:660px}
.step{position:absolute;width:240px;text-align:center;color:#fff}
.step svg{display:block;margin:0 auto}
.step h3{font-size:17px;font-weight:700;margin-top:18px}
.step p{font-size:12.5px;line-height:20px;color:#cfe7f3;margin-top:14px}
.step-arrow{position:absolute;top:318px}

/* contact */
.contact{top:3362px;height:497px;background:linear-gradient(90deg,#e4e8ee 0%,#eef1f4 50%,#dfe4ea 100%)}
.contact .section-title{top:52px;font-size:28px;color:var(--ink);font-weight:500}
.field{position:absolute;background:#fff;border:1px solid #cfd5dc;font-size:14px;color:#555b64;padding:14px 22px}
.contact .btn-outline{font-size:17px;color:var(--blue);background:transparent}

/* footer */
.site-footer{top:3859px;height:390px;background:var(--navy)}
.fcol{position:absolute;top:74px}
.fcol h4{font-size:15px;font-weight:500;color:#fff;margin-bottom:16px}
.fcol li{list-style:none;font-size:12.5px;color:#b8c0ce;line-height:24.7px}
.social li{display:flex;align-items:center;gap:9px}
.social li i{width:9px;height:9px;border-radius:50%;background:#d5dae3;display:inline-block}
.live-chat{position:absolute;left:677px;top:217px;width:155px;height:36px;background:var(--blue-bright);display:flex;align-items:center;color:#fff;font-size:12.5px;font-weight:700}
.live-chat .chat-icon{width:38px;height:36px;background:#fff;display:flex;align-items:center;justify-content:center;margin-right:16px}
.fdivider{position:absolute;left:145px;top:311px;width:885px;height:1px;background:#4d5a72}
.fbottom{position:absolute;top:336px;font-size:12px;color:#b8c0ce}
</style>
</head>
<body>

<div class="abs topbar">
  <ul><li>LOGIN</li><li>INTEGRATIONS</li><li>SUPPORT</li><li>RESOURCES</li></ul>
</div>

<header class="site-header">
  <div class="brand"><span class="brand-dot"></span>Harbor Lane PEO</div>
  <span class="nav-marker"></span>
  <nav class="main-nav">
    <a>ABOUT US</a><a>SERVICES</a><a>SOLUTION</a><a>TESTIMONIAL</a><a>COURSES</a><a>CONTACT</a>
  </nav>
</header>

<section class="hero">
  <div class="hero-photo" role="img" aria-label="Photo of a woman in glasses working on a laptop in a bright office"></div>
  <div class="hero-title">
    <div class="light">WE PROVIDE PAYROLL</div>
    <div class="bold">COMPENSATION</div>
    <div class="bold">PROCESSING</div>
  </div>
  <a class="btn-solid">LEARN MORE</a>
  <svg class="hero-arrow" style="left:38px" width="24" height="40" viewBox="0 0 24 40"><path d="M20 4 L6 20 L20 36" fill="none" stroke="#fff" stroke-width="4"/></svg>
  <svg class="hero-arrow" style="left:1140px" width="24" height="40" viewBox="0 0 24 40"><path d="M4 4 L18 20 L4 36" fill="none" stroke="#fff" stroke-width="4"/></svg>
  <svg class="hero-curve" viewBox="0 0 1200 120" preserveAspectRatio="none">
    <path d="M0 120 Q600 -10 1200 120 Z" fill="#fff"/>
    <path d="M60 108 Q600 8 1150 100" fill="none" stroke="#1a6fb5" stroke-width="4"/>
  </svg>
  <div class="emblem" style="left:573px;top:570px"><span></span></div>
</section>

<section class="services">
  <h2 class="section-title">OUR SERVICES</h2>
  <p class="lead" style="top:50px">Fusce tellus Sed metus augue convallis et vehicula ut pulvinar eu ante Integer orci tellus tristique vitae consequat nec porta vel lectus Nulla sit amet dui lectus cursus eu</p>

  <div class="service featured" style="left:143px;top:145px">
    <svg style="left:46px;top:26px" width="60" height="62" viewBox="0 0 60 62" fill="none" stroke="#1a80c4" stroke-width="2"><circle cx="26" cy="24" r="18"/><circle cx="26" cy="20" r="6"/><path d="M16 36 Q26 26 36 36"/><path d="M39 37 L52 54"/><path d="M46 10h10M46 16h8M46 22h10"/></svg>
    <h3 style="left:38px;top:115px">Recruiting</h3>
    <p style="left:38px;top:150px;width:230px">Fusce tellus Sed metus augue convallis et vehicula ut pulvinar eu ante Integer orci tellus tri</p>
  </div>
  <div class="service" style="left:478px;top:160px">
    <svg style="left:6px;top:0" width="60" height="62" viewBox="0 0 60 62" fill="none" stroke="#1a80c4" stroke-width="2"><circle cx="30" cy="18" r="12"/><path d="M8 60 V48 Q8 36 30 36 Q52 36 52 48 V60 Z"/><path d="M30 36 L30 60 M24 38 L30 46 L36 38"/></svg>
    <h3 style="left:6px;top:105px">Administrative<br>Onboarding</h3>
    <p style="left:6px;top:162px;width:230px">Fusce tellus Sed metus augue convallis et vehicula ut pulvi</p>
  </div>
  <div class="service" style="left:786px;top:168px">
    <svg style="left:0;top:0" width="62" height="60" viewBox="0 0 62 60" fill="none" stroke="#1a80c4" stroke-width="2"><rect x="22" y="2" width="36" height="26"/><path d="M28 22 L36 14 L42 18 L52 8"/><circle cx="10" cy="18" r="5"/><path d="M2 40 Q10 28 18 40"/><circle cx="20" cy="44" r="4"/><circle cx="34" cy="44" r="4"/><circle cx="48" cy="44" r="4"/><path d="M13 58 Q20 50 27 58 M27 58 Q34 50 41 58 M41 58 Q48 50 55 58"/></svg>
    <h3 style="left:6px;top:100px;width:290px">New hire training, ongoing training and development</h3>
    <p style="left:6px;top:153px;width:230px">Fusce tellus Sed metus augue convallis et vehicula ut</p>
  </div>

  <div class="service" style="left:178px;top:477px">
    <svg style="left:0;top:0" width="62" height="62" viewBox="0 0 62 62" fill="none" stroke="#1a80c4" stroke-width="2"><rect x="10" y="4" width="48" height="38" rx="3"/><path d="M10 14 H58 M18 26 H40 M18 32 H34"/><circle cx="16" cy="46" r="12" fill="#fff"/><path d="M16 39 V53 M20 42 Q16 40 13 43 Q14 46 17 46 Q20 47 19 50 Q16 52 12 50"/></svg>
    <h3 style="left:0;top:100px;width:270px">Payroll/compensation processing/services</h3>
    <p style="left:0;top:167px;width:230px">Fusce tellus Sed metus augue convallis et vehicula ut pu</p>
  </div>
  <div class="service" style="left:478px;top:477px">
    <svg style="left:2px;top:0" width="64" height="62" viewBox="0 0 64 62" fill="none" stroke="#1a80c4" stroke-width="2"><circle cx="14" cy="14" r="11"/><circle cx="14" cy="11" r="4"/><path d="M7 21 Q14 14 21 21"/><circle cx="46" cy="46" r="11"/><circle cx="46" cy="43" r="4"/><path d="M39 53 Q46 46 53 53"/><path d="M30 10 H50 V26 M46 22 L50 26 L54 22"/><path d="M32 50 H12 V34 M8 38 L12 34 L16 38"/></svg>
    <h3 style="left:0;top:100px">Employee<br>Relations</h3>
    <p style="left:0;top:152px;width:230px">Fusce tellus Sed metus augue convallis et vehicula ut pulvin</p>
  </div>
  <div class="service" style="left:786px;top:477px">
    <svg style="left:2px;top:0" width="64" height="62" viewBox="0 0 64 62" fill="none" stroke="#1a80c4" stroke-width="2"><path d="M4 4 H46 V58 H4 Z"/><rect x="12" y="12" width="14" height="12"/><path d="M30 14 H40 M30 20 H40 M12 32 H38 M12 40 H38 M12 48 H30"/><path d="M46 8 Q58 8 58 18 V52"/><path d="M54 22 Q50 20 50 24 Q50 27 54 27 Q58 28 56 32 Q53 33 50 31 M54 18 V35"/></svg>
    <h3 style="left:0;top:100px">Unemployment<br>Claim Facilitation</h3>
    <p style="left:0;top:152px;width:230px">Fusce tellus Sed metus augue convallis et vehicula</p>
  </div>

  <a class="btn-outline" style="left:498px;top:753px;width:217px;height:53px">VIEW ALL SERVICES</a>
</section>

<section class="testimonial">
  <div class="testimonial-photo" role="img" aria-label="Photo of a smiling woman in glasses at a desk in a busy office"></div>
  <h2>WHAT PEOPLE SAYS</h2>
  <blockquote>Fusce tellus Sed metus augue convallis et vehicula ut pulvinar eu ante Integer orci tellus tristique vitae consequat nec porta vel lectus Nulla sit amet diam aliquam enim Proin dui lectus cursus eu</blockquote>
  <div class="author"><b>By Author Name</b><br>Company Name</div>
  <div class="dots"><span></span><span></span><span></span><span></span></div>
  <svg class="abs" style="left:788px;top:244px" width="78" height="78" viewBox="0 0 78 78"><circle cx="39" cy="39" r="35" fill="rgba(0,0,0,.15)" stroke="#fff" stroke-width="5"/><path d="M31 24 L56 39 L31 54 Z" fill="#fff"/></svg>
</section>

<section class="courses">
  <h2 class="section-title">TRAINING CERTIFICATION COURSES</h2>

  <div class="course-photo" style="left:153px;top:158px;background:linear-gradient(135deg,#6e86a6,#3c5478)" role="img" aria-label="Photo of a man in glasses working at a laptop"></div>
  <div class="course-box" style="left:172px;top:338px">
    <h3>Fusce tellus Sed metus augue convallis</h3>
    <p>Curabitur vel dolor ultrices ipsum dictum tristique Praesent vitae lacus Ut</p>
  </div>

  <div class="course-photo" style="left:470px;top:162px;background:linear-gradient(135deg,#4a6fa8,#a3b6d4)" role="img" aria-label="Photo of a woman in glasses on a phone call at her desk"></div>
  <div class="course-box active" style="left:488px;top:342px">
    <h3>Fusce tellus Sed metus augue convallis</h3>
    <p>Curabitur vel dolor ultrices ipsum dictum tristique Praesent vitae lacus Ut</p>
  </div>

  <div class="course-photo" style="left:786px;top:165px;background:linear-gradient(135deg,#d3d8de,#8d97a5)" role="img" aria-label="Photo of a smiling man in glasses using a laptop"></div>
  <div class="course-box" style="left:804px;top:346px">
    <h3>Fusce tellus Sed metus augue convallis</h3>
    <p>Curabitur vel dolor ultrices ipsum dictum tristique Praesent vitae lacus Ut</p>
  </div>

  <a class="btn-outline" style="left:489px;top:526px;width:256px;height:53px">VIEW MORE COURSES</a>
</section>

<section class="get-started">
  <svg class="gs-curve" viewBox="0 0 1200 95" preserveAspectRatio="none"><path d="M0 0 H1200 V12 Q600 150 0 12 Z" fill="#fff"/></svg>
  <div class="emblem" style="left:573px;top:80px"><span></span></div>
  <h2>GET STARTED TODAY</h2>
  <p class="lead">Augiat in pede Fusce tellus Sed metus augue convallis et vehicula ut pulvinar eu ante Integer orci tellus tristique vitae consequat nec mauris viverra in gravida eu mattis in ante Morbi</p>

  <div class="step" style="left:184px;top:300px">
    <svg width="58" height="58" viewBox="0 0 58 58" fill="none" stroke="#fff" stroke-width="2"><circle cx="29" cy="29" r="8"/><circle cx="29" cy="8" r="6"/><circle cx="29" cy="50" r="6"/><circle cx="8" cy="29" r="6"/><circle cx="50" cy="29" r="6"/><circle cx="12" cy="12" r="4"/><circle cx="46" cy="46" r="4"/><path d="M29 14 V21 M29 37 V44 M14 29 H21 M37 29 H44"/></svg>
    <h3>GET CONNECT</h3>
    <p>At vehicula ut pulvinar eu ante Integer orci tellus tristique vitae consequat nec mauris</p>
  </div>
  <svg class="step-arrow" style="left:406px" width="40" height="20" viewBox="0 0 40 20" fill="none" stroke="#9fd3ea" stroke-width="2"><path d="M2 10 H36 M28 3 L36 10 L28 17"/></svg>
  <div class="step" style="left:480px;top:300px">
    <svg width="58" height="58" viewBox="0 0 58 58" fill="none" stroke="#fff" stroke-width="2"><rect x="18" y="2" width="22" height="14" rx="2"/><circle cx="10" cy="20" r="5"/><circle cx="48" cy="20" r="5"/><circle cx="29" cy="26" r="5"/><path d="M3 56 V34 Q10 28 17 34 V56 M41 56 V34 Q48 28 55 34 V56 M22 56 V40 Q29 33 36 40 V56"/></svg>
    <h3>MEET</h3>
    <p>At vehicula ut pulvinar eu ante Integer orci tellus tristique vitae consequat nec mauris</p>
  </div>
  <svg class="step-arrow" style="left:759px" width="40" height="20" viewBox="0 0 40 20" fill="none" stroke="#9fd3ea" stroke-width="2"><path d="M2 10 H36 M28 3 L36 10 L28 17"/></svg>
  <div class="step" style="left:789px;top:300px">
    <svg width="58" height="58" viewBox="0 0 58 58" fill="none" stroke="#fff" stroke-width="2"><path d="M22 36 Q30 12 54 4 Q46 28 22 36 Z"/><circle cx="40" cy="18" r="4"/><path d="M22 36 L14 30 L22 22 M22 36 L28 44 L36 36"/><path d="M14 44 L4 54 M18 48 L10 56"/></svg>
    <h3>ELEVATE</h3>
    <p>At vehicula ut pulvinar eu ante Integer orci tellus tristique vitae consequat nec mauris</p>
  </div>
</section>

<section class="contact" role="img" aria-label="Faded photo of colleagues in a meeting behind the contact form">
  <h2 class="section-title">CONTACT HARBOR LANE</h2>
  <div class="field" style="left:193px;top:120px;width:399px;height:52px">First Name</div>
  <div class="field" style="left:604px;top:120px;width:401px;height:52px">Last Name</div>
  <div class="field" style="left:193px;top:183px;width:399px;height:52px">Email address</div>
  <div class="field" style="left:604px;top:183px;width:401px;height:52px">Phone Number</div>
  <div class="field" style="left:193px;top:245px;width:812px;height:111px">Message</div>
  <a class="btn-outline" style="left:498px;top:377px;width:208px;height:55px">SUBMIT NOW</a>
</section>

<footer class="site-footer">
  <div class="fcol" style="left:147px"><h4>QUICK LINKS</h4><ul><li>About Us</li><li>Why Us</li><li>What We Do</li><li>Career</li><li>Our Services</li></ul></div>
  <div class="fcol" style="left:317px"><h4>WHO WE SERVE</h4><ul><li>Business Size</li><li>Industry</li><li>Partners</li></ul></div>
  <div class="fcol" style="left:492px"><h4>RESOURCES</h4><ul><li>Demos</li><li>What Others Say</li><li>Articles and Insights</li><li>Tools</li><li>Contact Us</li><li>Sitemap</li></ul></div>
  <div class="fcol" style="left:680px"><h4>CONTACT US</h4><ul><li>245 Harbor Row Suite 4B</li><li>Austin TX 78701</li><li>(512) 555 0148</li><li>info@harborlanepeo.com</li></ul></div>
  <div class="fcol social" style="left:921px"><h4>FOLLOW US</h4><ul><li><i></i>Community</li><li><i></i>Updates</li><li><i></i>Network</li><li><i></i>Gallery</li></ul></div>
  <a class="live-chat"><span class="chat-icon"><svg width="22" height="18" viewBox="0 0 22 18" fill="none" stroke="#0592cd" stroke-width="2"><path d="M3 2 H19 V12 H9 L4 16 V12 H3 Z"/></svg></span>LIVE CHAT &nbsp;&nbsp;›</a>
  <div class="fdivider"></div>
  <div class="fbottom" style="left:145px">© 2020 Harbor Lane PEO | All Rights Reserved | Disclaimer</div>
  <div class="fbottom" style="left:854px">Privacy &nbsp;|&nbsp; Legal &nbsp;|&nbsp; Sitemap</div>
</footer>

</body>
</html>
```